Tomasi's Pizzeria BOGO Promotion Pizza Flyer (Huron)

Pizzeria flyer promoting "under new management" and then the main point for this flyer is our Buy One Get One Free promotion on our pizzas (disclaimer: not valid for Jr Family Crust or Family Pizzas)(we reserve the right to cancel this promotion at any time)
This promotion has no limit and can be carryout or delivery. No coupon needed.
Looking for a fun bright flyer with our logo colors

Requirements
Must have
• Store Info
• 287 Marwick Rd. E
• Huron, OH
• 419-562-3870
• Open at 4pm Daily!

```html
<!DOCTYPE html>
<html lang="en">
<head>
<meta charset="utf-8">
<title>Tomasi's Pizzeria – Buy One Get One Free</title>
<link rel="stylesheet" href="https://fonts.googleapis.com/css2?family=Fredoka:wght@500;600;700&family=Lato:wght@300;400&display=swap">
<style>
  :root {
    --stage: #4a4c52;
    --wood-dark: #2a160c;
    --wood-mid: #4a2714;
    --wood-light: #5e3420;
    --cream: #ffffff;
    --orange: #f0a23a;
    --brand-red: #c8202c;
    --crust: #c98a44;
    --sauce: #b5462a;
    --cheese: #e7c24a;
  }
  * { margin: 0; padding: 0; box-sizing: border-box; }
  html, body {
    width: 1200px; height: 983px; overflow: hidden;
    background: var(--stage);
  }
  .flyer {
    position: absolute; left: 260px; top: 51px;
    width: 680px; height: 880px; overflow: hidden;
    background: linear-gradient(160deg, var(--wood-light) 0%, var(--wood-mid) 45%, var(--wood-dark) 100%);
    box-shadow: 0 20px 50px rgba(0,0,0,.45);
    font-family: "Fredoka", sans-serif;
    color: var(--cream);
  }
  .photo { position: absolute; border-radius: 50%; }
  .photo--top-greens {
    left: 250px; top: -40px; width: 150px; height: 120px;
    background: radial-gradient(circle at 40% 60%, #5c9a34 0%, #3a6a20 55%, rgba(58,106,32,0) 75%);
  }
  .photo--top-pizza {
    left: 430px; top: -30px; width: 240px; height: 240px;
    background: radial-gradient(circle, #c9572e 0%, var(--sauce) 55%, var(--crust) 80%, #8c5426 100%);
  }
  .photo--side-pizza {
    left: 420px; top: 500px; width: 260px; height: 260px;
    background: radial-gradient(circle, var(--cheese) 0%, #dcae3a 60%, var(--crust) 85%, #9c6428 100%);
  }
  .photo--main-pizza {
    left: 10px; top: 560px; width: 400px; height: 400px;
    background: radial-gradient(circle, #a8483a 0%, #8d3b2a 50%, #c58a4a 82%, #8a5226 100%);
  }
  .brand {
    position: absolute; left: 40px; top: 70px;
    display: flex; align-items: center; gap: 10px;
  }
  .brand__dot { width: 22px; height: 22px; border-radius: 50%; background: var(--brand-red); }
  .brand__name { font-size: 26px; font-weight: 600; color: var(--cream); }
  .headline {
    position: absolute; left: 40px; top: 175px;
    font-size: 40px; font-weight: 700; letter-spacing: 1px;
  }
  .headline__free {
    position: absolute; left: 36px; top: 205px;
    font-size: 128px; font-weight: 700; line-height: 1;
    color: var(--orange); letter-spacing: 2px;
  }
  .headline__free sup { font-size: 60px; vertical-align: top; position: relative; top: 6px; }
  .terms {
    position: absolute; left: 40px; top: 355px;
    font-size: 23px; font-weight: 600; line-height: 1.25; text-transform: uppercase;
  }
  .contact { position: absolute; left: 40px; top: 432px; }
  .contact__call { font-family: "Lato", sans-serif; font-weight: 300; font-size: 17px; }
  .contact__row { display: flex; align-items: center; gap: 20px; margin-top: 4px; }
  .contact__phone { display: flex; align-items: center; gap: 6px; font-size: 28px; font-weight: 600; }
  .contact__address { display: flex; align-items: center; gap: 5px; font-size: 15px; font-weight: 500; white-space: nowrap; }
  .contact__hours { font-size: 40px; font-weight: 700; margin-top: 4px; }
  .plus { position: absolute; left: 360px; top: 625px; }
  .fineprint {
    position: absolute; left: 440px; top: 790px; width: 230px;
    font-family: "Lato", sans-serif; font-size: 12px; line-height: 1.35;
  }
</style>
</head>
<body>
  <main class="flyer">
    <div class="photo photo--top-greens" role="img" aria-label="Fresh basil, tomatoes and spices"></div>
    <div class="photo photo--top-pizza" role="img" aria-label="Sliced margherita pizza on a board"></div>

    <div class="brand">
      <span class="brand__dot"></span>
      <span class="brand__name">Tomasi's Pizzeria</span>
    </div>

    <h1 class="headline">BUY ONE GET ONE</h1>
    <div class="headline__free">FREE<sup>*</sup></div>

    <p class="terms">No limit &amp; can be carryout or delivery<br>No coupon needed.</p>

    <section class="contact">
      <p class="contact__call">Call us NOW!!</p>
      <div class="contact__row">
        <span class="contact__phone">
          <svg width="18" height="18" viewBox="0 0 24 24" aria-hidden="true"><path fill="#fff" d="M6.6 10.8a15 15 0 0 0 6.6 6.6l2.2-2.2a1 1 0 0 1 1-.25 11.4 11.4 0 0 0 3.6.6 1 1 0 0 1 1 1V20a1 1 0 0 1-1 1A17 17 0 0 1 3 4a1 1 0 0 1 1-1h3.5a1 1 0 0 1 1 1c0 1.25.2 2.45.57 3.57a1 1 0 0 1-.25 1z"/></svg>
          419-562-3870
        </span>
        <span class="contact__address">
          <svg width="12" height="16" viewBox="0 0 12 16" aria-hidden="true"><path fill="#fff" d="M6 0a6 6 0 0 0-6 6c0 4.5 6 10 6 10s6-5.5 6-10a6 6 0 0 0-6-6zm0 8.2A2.2 2.2 0 1 1 6 3.8a2.2 2.2 0 0 1 0 4.4z"/></svg>
          287 Marwick Rd. E, Huron, OH
        </span>
      </div>
      <p class="contact__hours">Open at 4pm Daily!</p>
    </section>

    <div class="photo photo--side-pizza" role="img" aria-label="Pepperoni, mushroom and olive pizza"></div>
    <div class="photo photo--main-pizza" role="img" aria-label="Supreme pizza with mushrooms, onion, olives and basil"></div>

    <svg class="plus" width="46" height="46" viewBox="0 0 50 50" aria-hidden="true">
      <rect x="19" y="4" width="12" height="42" rx="3" fill="#fff"/>
      <rect x="4" y="19" width="42" height="12" rx="3" fill="#fff"/>
    </svg>

    <p class="fineprint">*not valid for Jr Family Crust or Family Pizzas<br>*we reserve the right to cancel this promotion at any time</p>
  </main>
</body>
</html>
```